"Dario Quillon" Business Card

Friends

My name is "Dario Quillon" and I need your help! I need a new business card for my personal use.

As background, "Dario Quillon" is actually an alias that I use when I meet women. Please use your creative skills to create an amazing business card for me to use!

In addition to including my name and contact details (see the "Must Have" section), you may wish to add a catchphrase or a title if you think it would help me :)

For background, please see:

http://www.dailybrightwire.com/2013/07/23/morton-feld-dario-quillon_n_5129847.html

Looking forward to seeing what you can do for me.

Hugs and kisses,

Dario Quillon [courtesy of PixelHarbor]

Target Market(s)

Adult women in New York City...or anywhere really.

Industry/Entity Type

Business

Requirements
Must have
• Please include the following details:

Dario Quillon
P: +1-555-3QUILLN
E: secrets@darioquillon-mail.com
Nice to have
• You might include a catchphrase, like "Quillon is my surname But you can call me Mr Smoothstep".

Or perhaps a title, like "Dario Quillon, Head of Sexy Times".

You're creative...I will leave the details to you my friends.
Should not have
• Any references to my actual name...because then, what's the point in using an alias?

```html
<!DOCTYPE html>
<html lang="en">
<head>
<meta charset="utf-8">
<title>Dario Quillon – Business Card</title>
<link rel="stylesheet" href="https://fonts.googleapis.com/css2?family=Fondamento&family=Open+Sans:ital,wght@0,400;1,400&display=swap">
<style>
  :root {
    --bg-left: #46494d;
    --bg-mid: #252628;
    --bg-right: #000000;
    --title-ink: #555555;
    --contact-ink: #c9ced3;
    --tagline-ink: #b6cd2f;
    --name-light: #b9b9b9;
    --name-dark: #4b4b4b;
  }
  html, body {
    margin: 0;
    padding: 0;
    width: 1200px;
    height: 720px;
    overflow: hidden;
    background: #000;
  }
  .card {
    position: relative;
    width: 1200px;
    height: 720px;
    overflow: hidden;
    font-family: "Open Sans", Arial, sans-serif;
  }
  .card-art {
    position: absolute;
    inset: 0;
    width: 1200px;
    height: 720px;
  }
  .title {
    position: absolute;
    margin: 0;
    font-style: italic;
    font-weight: 400;
    font-size: 64px;
    line-height: 1;
    letter-spacing: 0.07em;
    color: var(--title-ink);
    white-space: nowrap;
  }
  .title-line { position: absolute; }
  .title-line--first { left: 213px; top: 70px; }
  .title-line--second { left: 157px; top: 147px; }
  .name {
    position: absolute;
    left: 558px;
    top: 222px;
    margin: 0;
    font-family: "Fondamento", "Times New Roman", cursive;
    font-weight: 400;
    font-size: 88px;
    line-height: 1.1;
    letter-spacing: 0.03em;
    white-space: nowrap;
    background: linear-gradient(180deg, var(--name-light) 0%, #8a8a8a 45%, var(--name-dark) 55%, #7a7a7a 100%);
    -webkit-background-clip: text;
    background-clip: text;
    color: transparent;
  }
  .contact {
    position: absolute;
    left: 569px;
    top: 402px;
    margin: 0;
    font-size: 27px;
    line-height: 41px;
    letter-spacing: 0.05em;
    color: var(--contact-ink);
    font-style: normal;
    white-space: nowrap;
  }
  .contact-line { display: block; }
  .tagline {
    position: absolute;
    left: 524px;
    top: 636px;
    margin: 0;
    font-size: 32px;
    line-height: 32px;
    letter-spacing: 0.07em;
    color: var(--tagline-ink);
    white-space: nowrap;
  }
</style>
</head>
<body>
<main class="card">
  <svg class="card-art" viewBox="0 0 1125 675" preserveAspectRatio="none" aria-hidden="true">
    <defs>
      <linearGradient id="bg-fade" x1="0" y1="0" x2="1" y2="0">
        <stop offset="0" stop-color="#46494d"/>
        <stop offset="0.45" stop-color="#26272a"/>
        <stop offset="1" stop-color="#000000"/>
      </linearGradient>
      <linearGradient id="swoosh-fade" x1="0" y1="0" x2="0" y2="1">
        <stop offset="0" stop-color="#f2f2f2"/>
        <stop offset="0.5" stop-color="#c8c8c8"/>
        <stop offset="1" stop-color="#7d7d7d"/>
      </linearGradient>
      <linearGradient id="beam-fade" x1="0" y1="0" x2="0" y2="1">
        <stop offset="0" stop-color="#4f4c4b"/>
        <stop offset="1" stop-color="#8d8b8b"/>
      </linearGradient>
      <linearGradient id="lens-fade" x1="0" y1="0" x2="0" y2="1">
        <stop offset="0" stop-color="#ffffff"/>
        <stop offset="0.75" stop-color="#f7f7f7"/>
        <stop offset="1" stop-color="#e2e2e2"/>
      </linearGradient>
      <linearGradient id="stud-fill" x1="0" y1="0" x2="0" y2="1">
        <stop offset="0" stop-color="#bfbfbf"/>
        <stop offset="0.5" stop-color="#bfbfbf"/>
        <stop offset="0.5" stop-color="#5e5e5e"/>
        <stop offset="1" stop-color="#8a8a8a"/>
      </linearGradient>
      <pattern id="stud-row" x="583" y="0" width="33.4" height="675" patternUnits="userSpaceOnUse">
        <rect x="0" y="0" width="13" height="12" fill="url(#stud-fill)" stroke="#9a9a9a" stroke-width="0.8"/>
      </pattern>
    </defs>

    <rect class="backdrop" width="1125" height="675" fill="url(#bg-fade)"/>
    <path class="swoosh" d="M0,0 L96,0 C104,190 170,430 258,675 L232,675 C175,520 90,360 0,330 Z" fill="url(#swoosh-fade)"/>
    <path class="beam-edge" d="M96,0 L120,0 C130,230 205,450 262,675 L252,675 C180,450 104,220 96,0 Z" fill="#3c3b3b"/>
    <path class="beam" d="M112,0 L560,0 C595,210 470,430 420,675 L258,675 C200,450 120,240 112,0 Z" fill="url(#beam-fade)"/>
    <circle class="lens-rim" cx="337" cy="128" r="207" fill="#dfe6e8"/>
    <circle class="lens" cx="337" cy="128" r="195" fill="url(#lens-fade)"/>

    <rect class="stud-divider" x="583" y="340" width="490" height="12" fill="url(#stud-row)" transform="translate(0,-340) translate(0,340)"/>
    <rect class="stud-divider" x="583" y="484" width="490" height="12" fill="url(#stud-row)"/>
  </svg>

  <h2 class="title">
    <span class="title-line title-line--first">Head of</span>
    <span class="title-line title-line--second">Sexy Times</span>
  </h2>

  <h1 class="name">Dario Quillon</h1>

  <address class="contact">
    <span class="contact-line">eMail: secrets@darioquillon-mail.com</span>
    <span class="contact-line">Phone: +1-555-3QUILLN</span>
  </address>

  <p class="tagline">Dario Quillon is my name, but you<br>can call me Mr Smoothstep</p>
</main>
</body>
</html>
```